依頼詳細
企画内容や入れた欲しい文言は添付資料にあります。(A4で2枚分)
文字の大きさや赤字は私が強調したいと考えているイメージと捉えてください。
また、文言・キャッチ等の変更の提案は大歓迎です。是非勉強させてください!

イメージしている事
・女性がターゲットになっているような雰囲気。
・当たり障りのないというよりは、どこか振り切れているような個性的な雰囲気。
・「頑張ってやってくれそうね。」という印象を持ってもらいたい。
今回ワークテラスさんに依頼するのは、2回目ですが前回(下敷きのデザイン)は、ワークテラスさんの色々な提案により当初イメージしていたものよりいい物ができたので、色々な提案や質問は大歓迎です。

また、出来れば今回の依頼の中で、今後も定期的にデザインをお願いできる方がいればという事を兼ねているので、定期的に(大体「月1」位のペース)お願いできる方はその旨お伝えください。

私が選考するポイント
・キャッチやレイアウト等、ターゲットからのレスポンスがありそうか?
私はチラシは如何にして見て読んだ瞬間にアクション(問い合わせ)を起こさせるかがポイントだと思っています。
・レスポンスの速さ(私は速くないですが)等の対応
記載項目
屋号:学習塾 ミナリオ
電話番号:047-513-8847
URL:http://minario-juku.jp/
※ 二次元コードとロゴは添付資料よりおとりください。
サイズ
B4
ページ数
両面
希望イメージ
シンプル 複雑
単色 カラフル
暗い 明るい
日常 高級
遊び心 厳粛
未来的 伝統的
女性的 男性的
希望する色
大きな希望はないですが、塾のイメージはオレンジです。
納品ファイル
• 高解像度JPG (.jpg)
• イラストレーター形式 (.ai)
• フォトショップ形式 (.psd)
補足説明
今回のチラシでは、塾長をある程度前面に出した形にしようと思っているので、
「ここにこんなポーズの写真をいれましょう!」
などのご提案も受け付けます。
言っていただければ、はめ込みもしやすいように白バックで撮ってお渡しします。

また、チラシの依頼は初めてなので説明の足りない箇所等あると思いますので、
その際はお手数ですが、ご質問ください。
キャンペーン面の下部に
「HPに『無料体験者の感想』を掲載しています」
とHPに誘導する仕組みを作成してください。
塾長の写真をアップしました。
ご確認ください。
たくさんのご提案ありがとうございました。
依頼の段階でもお伝えした通り、できれば今後も定期的にお願いできる方が希望です。
定期的な依頼が可能なのに、その旨お伝えいただいていない方はメッセージ等で、その旨ご連絡ください。

選定段階(修正依頼等)に入りましたら、またこの欄にてご報告させていただきます。
(少なくとも金曜日までにはアクションをおこします。)

本当にたくさんのご提案ありがとうございました。
■ 選んだ理由

私の当初のイメージ(熱意がありそう・ちゃんとした塾でありそう)
に、一番近かった事が最大の決め手でした。
また、私が添付したデータはただ腕組みをしている写真でしたが、
動きのある写真の方がいいなぁと、漠然には感じていた所も大きいかと思います。

■ 提案者全員のお礼・コメント

この度は、弊社の依頼にご提案いただき誠にありがとうございました。
正直、選考するのにかなり悩みました。
私が、原案の中で気になっていた箇所をうまくまとめていただいた方、
文言の言い回しの修正の仕方など、とても勉強になりました。
また、依頼をさせていただく際には、是非ご提案いただければと思います。

```html
<!DOCTYPE html>
<html lang="ja">
<head>
<meta charset="utf-8">
<title>中間特講 | 学習塾 ミナリオ</title>
<link rel="stylesheet" href="https://fonts.googleapis.com/css2?family=Noto+Sans+JP:wght@400;700;900&display=swap">
<style>
:root{
  --red:#e3141e;
  --orange:#f08a00;
  --yellow:#ffd21a;
  --green:#2f8a3a;
  --deep-green:#1f6b2c;
  --pale-green:#e9f3e1;
  --ink:#1a1a1a;
  --white:#ffffff;
}
*{margin:0;padding:0;box-sizing:border-box}
html,body{width:849px;height:1200px;overflow:hidden;background:var(--white)}
body{font-family:"Noto Sans JP",sans-serif;color:var(--ink)}
.flyer{position:relative;width:849px;height:1200px;overflow:hidden;background:var(--white)}
.photo{position:absolute;left:0;top:0;width:849px;height:880px;
  background:linear-gradient(180deg,#ffffff 0%,#f4f8fb 18%,#dbe9f1 40%,#b9d39a 62%,#6e9a46 80%,#3f6e2a 100%)}
.abs{position:absolute}
.target{left:20px;top:20px;background:var(--red);color:var(--white);font-weight:700;font-size:21px;padding:3px 12px;letter-spacing:.02em;white-space:nowrap}
.brand{left:648px;top:24px;width:178px;height:88px;display:flex;align-items:center;justify-content:center;gap:8px;background:var(--white);border:3px solid var(--green);white-space:nowrap}
.brand-square{flex:none;width:16px;height:16px;background:var(--green)}
.brand-name{font-weight:900;font-size:33px;color:var(--green);line-height:1}
.arrow{left:60px;top:80px;width:520px;height:260px}
.catch-1{left:22px;top:56px;font-size:58px;font-weight:900;letter-spacing:-.02em;white-space:nowrap}
.catch-2{left:84px;top:112px;font-size:132px;font-weight:900;color:var(--red);line-height:1.05;letter-spacing:-.04em;-webkit-text-stroke:4px var(--white);paint-order:stroke fill;white-space:nowrap}
.catch-2 small{font-size:98px}
.catch-3{left:64px;top:248px;font-size:58px;font-weight:900;-webkit-text-stroke:3px var(--white);paint-order:stroke fill;white-space:nowrap}
.lead{left:574px;top:130px;font-size:30px;font-weight:900;color:var(--red);white-space:nowrap}
.course{left:574px;top:170px;background:var(--red);color:var(--white);font-weight:700;font-size:21px;padding:2px 8px;white-space:nowrap}
.title{left:584px;top:204px;width:250px;text-align:center;line-height:1}
.title .kanji{display:block;font-size:118px;font-weight:900;color:var(--red);-webkit-text-stroke:4px var(--white);paint-order:stroke fill}
.title .ruby{display:block;font-size:22px;font-weight:700;color:var(--red);margin:4px 0}
.title-note{left:604px;top:482px;font-size:14px;font-weight:700;color:var(--red);white-space:nowrap}
.slogan{left:26px;top:420px;font-size:32px;font-weight:900;color:var(--green);line-height:1.4;-webkit-text-stroke:3px var(--white);paint-order:stroke fill}
.guarantees{left:22px;top:712px;width:616px;height:72px;display:flex;gap:6px}
.guarantee{flex:1;min-width:0;background:var(--white);border:3px solid var(--red);padding:4px 4px;text-align:center;display:flex;flex-direction:column;justify-content:center}
.guarantee-label{font-size:11px;font-weight:700;line-height:1.3;white-space:nowrap}
.guarantee-value{font-size:36px;font-weight:900;color:var(--red);line-height:1.1;white-space:nowrap}
.guarantee-value span{font-size:17px;color:var(--ink)}
.refund{left:22px;top:788px;width:616px;background:var(--red);color:var(--white);font-size:15.5px;font-weight:900;text-align:center;padding:4px 0;white-space:nowrap;line-height:1.4}
.refund mark{background:var(--yellow);color:var(--red);padding:0 3px}
.refund-note{left:22px;top:826px;width:616px;font-size:12px;color:var(--white);font-weight:700;white-space:nowrap}
.deadline{left:650px;top:712px;width:186px;height:150px;background:var(--deep-green);border:3px solid var(--white);text-align:center;padding-top:8px}
.deadline-label{color:var(--white);font-size:26px;font-weight:900}
.deadline-date{margin:6px auto 0;width:160px;background:var(--white);color:var(--red);font-size:64px;font-weight:900;line-height:1.2}
.info{position:absolute;left:0;top:876px;width:849px;height:324px;background:var(--green);padding:14px 20px}
.info-table{position:absolute;left:20px;top:14px;width:410px}
.row{display:flex;align-items:center;gap:10px;margin-bottom:6px}
.row-label{flex:none;width:64px;background:var(--white);color:var(--green);font-size:17px;font-weight:900;text-align:center;padding:2px 0}
.row-value{color:var(--white);font-size:34px;font-weight:900;line-height:1.1;white-space:nowrap}
.row-value.small{font-size:22px}
.row-value small{font-size:17px}
.note{color:var(--white);font-size:12px;line-height:1.45;margin:0 0 8px 74px}
.contact{position:absolute;left:450px;top:14px;width:380px}
.contact-head{display:flex;align-items:center;gap:8px}
.contact-tag{background:var(--white);color:var(--green);font-size:16px;font-weight:900;padding:2px 6px;line-height:1.2}
.phone{display:flex;align-items:center;gap:6px;background:var(--white);border-radius:6px;padding:2px 8px;color:var(--orange);font-size:40px;font-weight:900;line-height:1.2;white-space:nowrap}
.phone svg{width:34px;height:34px;fill:var(--orange)}
.contact-note{color:var(--white);font-size:12px;margin:6px 0 8px}
.url{background:var(--white);border-radius:6px;color:var(--orange);font-size:26px;font-weight:900;padding:4px 10px;text-align:center;white-space:nowrap}
.phone.second{color:var(--green);margin-top:4px}
.phone.second svg{fill:var(--green)}
</style>
</head>
<body>
<main class="flyer">
  <div class="photo" role="img" aria-label="公園で手をつないでジャンプする女子中学生二人の写真"></div>

  <p class="abs target">桜ヶ丘中・緑町中・若葉台中に通学中のお子さま対象</p>

  <div class="abs brand">
    <span class="brand-square"></span>
    <span class="brand-name">ミナリオ</span>
  </div>

  <svg class="abs arrow" viewBox="0 0 520 260" aria-hidden="true">
    <polygon points="0,240 380,70 366,40 500,20 430,135 412,108 30,260" fill="var(--yellow)"/>
  </svg>

  <p class="abs catch-1">中間テスト</p>
  <p class="abs catch-2">20<small>点</small>UP</p>
  <p class="abs catch-3">保証します!</p>

  <p class="abs lead">塾長直伝!</p>
  <p class="abs course">中間テスト短期特訓講座</p>
  <h1 class="abs title">
    <span class="kanji">中間</span>
    <span class="ruby">ちゅうかんとっこう</span>
    <span class="kanji">特講</span>
  </h1>
  <p class="abs title-note">※各中学校の試験日程までの期間</p>

  <p class="abs slogan">数学嫌いな君達よ!<br>いつまでも<br>逃げちゃダメだ!</p>

  <div class="abs guarantees">
    <div class="guarantee">
      <p class="guarantee-label">入学して最初の中間テストで</p>
      <p class="guarantee-value">90点<span>以上保証</span></p>
    </div>
    <div class="guarantee">
      <p class="guarantee-label">1年生の後期期末テストの成績から</p>
      <p class="guarantee-value">+20点<span>保証</span></p>
    </div>
    <div class="guarantee">
      <p class="guarantee-label">2年生の後期期末テストの成績から</p>
      <p class="guarantee-value">+20点<span>保証</span></p>
    </div>
  </div>
  <p class="abs refund">成績が上がらなかった場合は、<mark>授業料は全額返金!</mark> 無料で補習授業を行います。</p>
  <p class="abs refund-note">※保証の条件は講座の全日程に出席し、宿題をすべて提出した場合に限ります。</p>

  <div class="abs deadline">
    <p class="deadline-label">申込み締切</p>
    <p class="deadline-date">5/10</p>
  </div>

  <section class="info">
    <div class="info-table">
      <div class="row"><span class="row-label">料金</span><span class="row-value">10,000円<small>(税込)</small></span></div>
      <p class="note">※教材費込み。追加の費用は一切かかりません。</p>
      <div class="row"><span class="row-label">定員</span><span class="row-value">10名<small>(先着順)</small></span></div>
      <div class="row"><span class="row-label">内容</span><span class="row-value small">個別指導+直前試験対策授業</span></div>
      <p class="note">合計720分(12時間)<br>※日程は各中学校の試験日に合わせて決定します。<br>※詳しくはお電話またはホームページでご確認ください。</p>
    </div>
    <div class="contact">
      <div class="contact-head"><span class="contact-tag">お申込み</span></div>
      <p class="phone">
        <svg viewBox="0 0 24 24" aria-hidden="true"><path d="M6.6 10.8a15.1 15.1 0 0 0 6.6 6.6l2.2-2.2a1 1 0 0 1 1-.25 11.4 11.4 0 0 0 3.6.57 1 1 0 0 1 1 1V20a1 1 0 0 1-1 1A17 17 0 0 1 3 4a1 1 0 0 1 1-1h3.5a1 1 0 0 1 1 1c0 1.250.2 2.450.57 3.57a1 1 0 0 1-.25 1z"/></svg>
        047-513-8847
      </p>
      <p class="contact-note">上記番号までご連絡の上、「中間特講申込み」とお伝えください。</p>
      <p class="url">http://minario-juku.jp/</p>
      <p class="contact-note">お問合せフォームからも受け付けております。<br>お名前・ご連絡先・「中間特講申込み」と明記してください。</p>
      <p class="phone second">
        <svg viewBox="0 0 24 24" aria-hidden="true"><path d="M6.6 10.8a15.1 15.1 0 0 0 6.6 6.6l2.2-2.2a1 1 0 0 1 1-.25 11.4 11.4 0 0 0 3.6.57 1 1 0 0 1 1 1V20a1 1 0 0 1-1 1A17 17 0 0 1 3 4a1 1 0 0 1 1-1h3.5a1 1 0 0 1 1 1c0 1.250.2 2.450.57 3.57a1 1 0 0 1-.25 1z"/></svg>
        047-513-8850
      </p>
    </div>
  </section>
</main>
</body>
</html>
```